Orva Business Card

we need a business card for flooring business called Orva Flooring, the design should be black and white. we have 2 locations

Ashvale Showroom
527 Kellerman Road,
Ashvale VIC 3158

Corrindale Showroom
462 Bramwell Hwy,
Corrindale VIC 3217

email : sales@orvaflooring.com.au
(03) 9471 2830

Please inform we sell , Laminate, Hybrid, Timber, carpet and commercial flooring

```html
<!DOCTYPE html>
<html lang="en">
<head>
<meta charset="UTF-8">
<title>Orva Flooring Business Card</title>
<link rel="stylesheet" href="https://fonts.googleapis.com/css2?family=Montserrat:wght@400;700&display=swap">
<style>
  :root {
    --page-bg: #7f99bb;
    --card-white: #ffffff;
    --card-black: #232323;
    --ink-dark: #262626;
    --ink-light: #f2f2f2;
    --ink-muted: #cfcfcf;
  }
  * { box-sizing: border-box; margin: 0; padding: 0; }
  html, body {
    width: 1200px;
    height: 876px;
    overflow: hidden;
  }
  body {
    background: var(--page-bg);
    font-family: "Montserrat", sans-serif;
    display: flex;
    align-items: center;
    justify-content: center;
    gap: 40px;
  }
  .card {
    width: 540px;
    height: 330px;
    position: relative;
    box-shadow: 0 10px 24px rgba(0, 0, 0, 0.22);
  }

  /* Front */
  .card-front {
    background: var(--card-white);
    display: flex;
    align-items: center;
    justify-content: center;
  }
  .brand-front {
    display: flex;
    align-items: center;
    gap: 14px;
    color: var(--ink-dark);
    font-size: 36px;
    font-weight: 400;
    letter-spacing: 3px;
    text-transform: uppercase;
  }
  .brand-dot {
    width: 14px;
    height: 14px;
    border-radius: 50%;
    background: var(--ink-dark);
  }

  /* Back */
  .card-back {
    background: var(--card-black);
    color: var(--ink-light);
    display: grid;
    grid-template-columns: 1fr 1fr;
    padding: 34px 30px 30px 34px;
  }
  .identity {
    display: flex;
    flex-direction: column;
    align-items: center;
    text-align: center;
  }
  .holder-name {
    font-size: 17px;
    font-weight: 700;
    letter-spacing: 1px;
    text-transform: uppercase;
  }
  .holder-role {
    font-size: 10px;
    color: var(--ink-muted);
    margin-top: 2px;
  }
  .brand-back {
    margin-top: 42px;
    font-size: 24px;
    font-weight: 400;
    letter-spacing: 2px;
    text-transform: uppercase;
    color: var(--ink-light);
  }
  .services {
    margin-top: 34px;
    font-size: 11px;
    line-height: 1.6;
    letter-spacing: 0.4px;
    text-transform: uppercase;
    color: var(--ink-light);
  }
  .contacts {
    list-style: none;
    display: flex;
    flex-direction: column;
    gap: 14px;
    padding-left: 26px;
    padding-top: 50px;
  }
  .contact-item {
    display: flex;
    align-items: flex-start;
    gap: 10px;
    font-size: 12px;
    line-height: 1.4;
  }
  .contact-icon {
    flex: none;
    width: 20px;
    height: 20px;
  }
  .showroom + .showroom { margin-top: 10px; }
</style>
</head>
<body>

  <section class="card card-front" aria-label="Card front">
    <div class="brand-front"><span class="brand-dot"></span>Orva Flooring</div>
  </section>

  <section class="card card-back" aria-label="Card back">
    <div class="identity">
      <p class="holder-name">Daniel Harte</p>
      <p class="holder-role">Director</p>
      <p class="brand-back">Orva Flooring</p>
      <p class="services">Laminate, Hybrid, Timber,<br>Carpet and Commercial Flooring</p>
    </div>

    <ul class="contacts">
      <li class="contact-item">
        <svg class="contact-icon" viewBox="0 0 20 20" aria-hidden="true">
          <circle cx="10" cy="10" r="10" fill="#f2f2f2"/>
          <path d="M6.5 5.5h2l1 2.5-1.3 1a6 6 0 0 0 2.8 2.8l1-1.3 2.5 1v2a1 1 0 0 1-1 1A8 8 0 0 1 5.5 6.5a1 1 0 0 1 1-1z" fill="#232323"/>
        </svg>
        <span>(03) 9471 2830</span>
      </li>
      <li class="contact-item">
        <svg class="contact-icon" viewBox="0 0 20 20" aria-hidden="true">
          <circle cx="10" cy="10" r="10" fill="#f2f2f2"/>
          <rect x="5" y="6.5" width="10" height="7" fill="none" stroke="#232323" stroke-width="1.3"/>
          <path d="M5 6.5l5 4 5-4" fill="none" stroke="#232323" stroke-width="1.3"/>
        </svg>
        <span>sales@orvaflooring.com.au</span>
      </li>
      <li class="contact-item">
        <svg class="contact-icon" viewBox="0 0 20 20" aria-hidden="true">
          <circle cx="10" cy="10" r="10" fill="#f2f2f2"/>
          <path d="M10 4.5a3.6 3.6 0 0 1 3.6 3.6c0 2.7-3.6 6.9-3.6 6.9S6.4 10.8 6.4 8.1A3.6 3.6 0 0 1 10 4.5z" fill="#232323"/>
          <circle cx="10" cy="8.1" r="1.3" fill="#f2f2f2"/>
        </svg>
        <div>
          <p class="showroom">Ashvale Showroom<br>527 Kellerman Road,<br>Ashvale VIC 3158</p>
          <p class="showroom">Corrindale Showroom,<br>462 Bramwell Hwy,<br>Corrindale VIC 3217</p>
        </div>
      </li>
    </ul>
  </section>

</body>
</html>
```